Company Website

We require an online clothing store website for construction workwear.
It needs to be easy to read, user friendly, easy to navigate purchasing.
We are after designs incorporating our recently design logo, and colour combinations black white and orange (same as the company logo). Needs to highlight quality, safety and products. Any ideas around highlighting branding are welcome.

Target Market(s)

Construction workers and businesses.

Industry/Entity Type

Construction

Coding

Coded - Design and coding required

Number of Pages Required

5+ page

Colors
EE7325
F08F49
F5BC92
FAE3D3
FDF4ED

Requirements
Must have
• Include all pictures, prices and details of the products we sell. See PDF uploaded to brief.
Nice to have
• Simple access to purchase items. Easy to navigate website layout.

```html
<!DOCTYPE html>
<html lang="en">
<head>
<meta charset="utf-8">
<title>Steelguard Workwear</title>
<link href="https://fonts.googleapis.com/css2?family=Michroma&family=Poppins:wght@400;500;600;700&display=swap" rel="stylesheet">
<style>
:root{
  --orange:#f15a0e;
  --black:#000;
  --ink:#1c1c1c;
  --white:#fff;
  --grey:#f2f2f2;
  --muted:#555;
  --footer:#000;
  --footer-bar:#111;
  --hero-a:#6d6d68;
  --hero-b:#3e3f3a;
}
*{box-sizing:border-box;margin:0;padding:0}
html,body{width:1200px;height:3911px;overflow:hidden}
body{position:relative;font-family:'Poppins',sans-serif;color:var(--ink);background:var(--white)}
.abs{position:absolute}
.display{font-family:'Michroma',sans-serif;white-space:nowrap;font-weight:400}
/* header */
.site-header{left:0;top:0;width:1200px;height:123px;background:var(--white)}
.brand{font-family:'Poppins',sans-serif;font-weight:700;color:var(--orange);font-size:34px;letter-spacing:2px;line-height:1}
.brand small{display:block;font-size:13px;letter-spacing:7px;margin-top:4px}
.site-header .brand{left:76px;top:44px}
.nav a{position:absolute;top:61px;font-size:13px;color:var(--ink);text-decoration:none}
.nav a.active{color:var(--orange);border-bottom:2px solid var(--orange);padding:0 4px 8px}
.badge{left:1046px;top:49px;width:15px;height:15px;border-radius:50%;background:var(--orange);color:#fff;font-size:10px;text-align:center;line-height:15px}
/* hero */
.hero{left:0;top:123px;width:1200px;height:814px;background:linear-gradient(100deg,var(--hero-b) 0%,var(--hero-a) 55%,#8a8a70 100%)}
.hero h2{position:absolute;left:76px;color:#fff;font-family:'Michroma',sans-serif;font-weight:400;white-space:nowrap;line-height:1}
.btn-dark{background:#000;color:#fff;font-weight:600;font-size:19px;display:flex;align-items:center;justify-content:center;text-decoration:none}
.dots span{position:absolute;top:0;width:12px;height:12px;border-radius:50%;background:#bbb}
/* features */
.features{left:78px;top:830px;width:1050px;height:158px;background:#fff;box-shadow:0 3px 14px rgba(0,0,0,.15)}
.feature{position:absolute;top:52px;display:flex;gap:10px}
.feature .ico{width:58px;height:58px;border-radius:50%;background:var(--orange);display:flex;align-items:center;justify-content:center;flex:none}
.feature h4{font-size:13px;font-weight:600;margin-top:4px}
.feature p{font-size:9.5px;line-height:13px;color:var(--muted);margin-top:4px}
/* section titles */
.sec-title{left:0;width:1200px;text-align:center;color:var(--orange);line-height:1}
.sec-sub{font-family:'Michroma',sans-serif;font-size:20px;letter-spacing:7px;color:#000;white-space:nowrap;line-height:1}
.rule{height:2px;background:#000}
/* products */
.card{top:1204px;width:248px;height:314px;background:#fff;box-shadow:0 2px 10px rgba(0,0,0,.14)}
.card .photo{height:203px}
.stars{color:#f5b800;font-size:13px;letter-spacing:1px}
.card .stars{position:absolute;left:26px;top:218px}
.card h3{position:absolute;left:26px;top:238px;font-size:14px;font-weight:600}
.card .bar{position:absolute;left:0;bottom:0;width:100%;height:36px;border-top:1px solid #e3e3e3;display:flex}
.card .bar div{width:57px;border-right:1px solid #e3e3e3;display:flex;align-items:center;justify-content:center}
.card .bar .price{flex:1;border:none;background:var(--orange);color:#fff;font-size:15px;font-weight:500}
.btn-outline{border:2px solid #000;background:#fff;font-size:13px;display:flex;align-items:center;justify-content:center;color:#000;text-decoration:none}
/* promo */
.promo{left:0;top:1705px;width:1200px;height:460px;background:var(--grey)}
.btn-orange{background:var(--orange);color:#fff;font-weight:600;display:flex;align-items:center;justify-content:center;text-decoration:none}
/* testimonials */
.review{top:2388px;width:278px;height:275px;background:#fff;box-shadow:0 2px 12px rgba(0,0,0,.12)}
.review .stars{position:absolute;left:34px;top:35px}
.review p{position:absolute;left:34px;top:66px;width:210px;font-size:13.5px;line-height:19px;color:var(--muted);text-align:justify}
.review hr{position:absolute;left:34px;top:172px;width:210px;border:none;border-top:1px solid #ddd}
.review .avatar{position:absolute;left:30px;top:188px;width:56px;height:56px;border-radius:50%;background:linear-gradient(#c9c4be,#7d746c)}
.review .who{position:absolute;left:100px;top:206px;font-size:14px;font-weight:600}
.quote{width:46px;height:46px;border-radius:50%;background:var(--orange);display:flex;align-items:center;justify-content:center}
/* gallery */
.gallery{left:0;top:2847px;width:1200px;height:375px;background:var(--grey)}
.gallery .tile{top:67px;width:232px;height:232px}
.arrow{top:190px;width:48px;height:48px;border-radius:50%;display:flex;align-items:center;justify-content:center}
/* newsletter + footer */
.footer{left:0;top:3475px;width:1200px;height:436px;background:var(--footer)}
.newsbox{left:232px;top:3430px;width:735px;height:148px;background:#fff}
.input{left:313px;top:3461px;width:567px;height:65px;border:1px solid #ddd;border-radius:33px;font-size:13px;color:#777;padding:22px 36px}
.col h5{position:absolute;color:var(--orange);font-size:14px;font-weight:600}
.col ul{position:absolute;list-style:none;color:#fff;font-size:13.5px}
.col li{height:26px;padding-left:22px;position:relative}
.col li::before{content:"›";position:absolute;left:2px;top:-3px;font-size:18px}
.contact{position:absolute;left:857px;color:#fff;font-size:13.5px;line-height:17px;display:flex;gap:16px}
.contact .ci{width:26px;height:26px;background:var(--orange);border-radius:4px;display:flex;align-items:center;justify-content:center;flex:none;margin-top:3px}
.social span{position:absolute;top:3760px;width:28px;height:28px;background:var(--orange);border-radius:4px}
.bottom{left:0;top:3858px;width:1200px;height:53px;background:var(--footer-bar);color:#fff;font-size:12px}
.pay span{position:absolute;top:18px;width:30px;height:18px;border-radius:2px}
</style>
</head>
<body>

<header class="site-header abs">
  <div class="brand abs">STEELGUARD<small>WORKWEAR</small></div>
  <nav class="nav">
    <a class="active" href="#" style="left:506px">HOME</a>
    <a href="#" style="left:582px">SHOP</a>
    <a href="#" style="left:650px">PRODUCTS</a>
    <a href="#" style="left:753px">ABOUT US</a>
    <a href="#" style="left:851px">FAQ</a>
    <a href="#" style="left:910px">CONTACT US</a>
  </nav>
  <svg class="abs" style="left:1026px;top:56px" width="26" height="22" viewBox="0 0 26 22"><path d="M0 2h5l4 12h13l3-9H8" fill="none" stroke="#000" stroke-width="2.5"/><path d="M8 5h17l-3 9H10z"/><circle cx="11" cy="19" r="2"/><circle cx="20" cy="19" r="2"/></svg>
  <div class="badge abs">0</div>
  <svg class="abs" style="left:1069px;top:54px" width="22" height="22" viewBox="0 0 22 22"><circle cx="11" cy="6" r="5.5"/><path d="M0 22c0-7 5-10 11-10s11 3 11 10z"/></svg>
  <svg class="abs" style="left:1105px;top:56px" width="20" height="20" viewBox="0 0 20 20"><circle cx="8" cy="8" r="6.5" fill="none" stroke="#000" stroke-width="1.8"/><path d="M13 13l6 6" stroke="#000" stroke-width="2"/></svg>
</header>

<section class="hero abs" role="img" aria-label="Construction worker in hard hat and high-visibility vest checking a clipboard">
  <h2 style="top:254px;font-size:28px">HARD WORKING</h2>
  <h2 style="top:296px;font-size:64px;color:var(--orange)">WORKWEAR</h2>
  <h2 style="top:377px;font-size:28px">FOR HARD WORKING PEOPLE</h2>
  <a class="btn-dark abs" href="#" style="left:76px;top:447px;width:190px;height:68px">SHOP NOW</a>
  <div class="dots abs" style="left:568px;top:648px">
    <span style="left:0;background:#fff"></span><span style="left:17px"></span><span style="left:34px"></span><span style="left:51px"></span>
  </div>
</section>

<section class="features abs">
  <div class="feature" style="left:48px"><div class="ico"><svg width="30" height="20" viewBox="0 0 30 20" fill="#fff"><rect x="0" y="2" width="18" height="12"/><path d="M19 6h6l4 5v3H19z"/><circle cx="6" cy="16" r="3"/><circle cx="23" cy="16" r="3"/></svg></div><div><h4>FREE SHIPPING</h4><p>Lorem ipsum dolor sit amet,<br>consectetur adipiscing elit</p></div></div>
  <div class="feature" style="left:296px"><div class="ico"><svg width="30" height="22" viewBox="0 0 30 22" fill="#fff"><rect x="0" y="3" width="18" height="12"/><path d="M19 7h6l4 5v3H19z"/><circle cx="6" cy="18" r="3"/><circle cx="23" cy="18" r="3"/></svg></div><div><h4>FAST DELIVERY</h4><p>Lorem ipsum dolor sit amet,<br>consectetur adipiscing elit</p></div></div>
  <div class="feature" style="left:542px"><div class="ico"><svg width="24" height="20" viewBox="0 0 24 20" fill="none" stroke="#fff" stroke-width="2.4"><path d="M2 6h19M16 1l5 5-5 5M22 14H3M8 9l-5 5 5 5"/></svg></div><div><h4>RETURN &amp; EXCHANGE</h4><p>Lorem ipsum dolor sit amet,<br>consectetur adipiscing elit</p></div></div>
  <div class="feature" style="left:798px"><div class="ico"><svg width="26" height="26" viewBox="0 0 26 26" fill="#fff"><path d="M3 14a10 10 0 0 1 20 0" fill="none" stroke="#fff" stroke-width="2.4"/><rect x="1" y="13" width="5" height="8" rx="2"/><rect x="20" y="13" width="5" height="8" rx="2"/><circle cx="13" cy="15" r="5"/></svg></div><div><h4>24/7 SUPPORT</h4><p>Lorem ipsum dolor sit amet,<br>consectetur adipiscing elit</p></div></div>
</section>

<h2 class="sec-title display abs" style="top:1088px;font-size:37px">OUR PRODUCTS</h2>
<div class="rule abs" style="left:386px;top:1140px;width:226px"></div>
<div class="sec-sub abs" style="left:622px;top:1130px">SHOP NOW</div>

<article class="card abs" style="left:76px"><div class="photo" role="img" aria-label="Worker in orange high visibility clothing beside a rack of workwear" style="background:linear-gradient(135deg,#3a2a25,#c8582a 55%,#6e3b2a)"></div><div class="stars">★★★★★</div><h3>High Visibility Clothing</h3><div class="bar"><div>⇆</div><div>♥</div><div>🛒</div><div class="price">$400.00</div></div></article>
<article class="card abs" style="left:343px"><div class="photo" role="img" aria-label="Pair of red leather protective gloves" style="background:linear-gradient(135deg,#dfe3e8,#b6524a 55%,#d5dae0)"></div><div class="stars">★★★★★</div><h3>Protective Gloves</h3><div class="bar"><div>⇆</div><div>♥</div><div>🛒</div><div class="price">$100.00</div></div></article>
<article class="card abs" style="left:610px"><div class="photo" role="img" aria-label="Pair of worn leather safety boots" style="background:linear-gradient(135deg,#b9c4d0,#4c3f2c 55%,#b9c4d0)"></div><div class="stars">★★★★★</div><h3>Safety Footwear</h3><div class="bar"><div>⇆</div><div>♥</div><div>🛒</div><div class="price">$200.00</div></div></article>
<article class="card abs" style="left:876px"><div class="photo" role="img" aria-label="Worker wearing white protective helmet and ear defenders" style="background:linear-gradient(180deg,#2f7ec9,#d9c22c 60%,#f0f0f0)"></div><div class="stars">★★★★★</div><h3>Protective Helmet</h3><div class="bar"><div>⇆</div><div>♥</div><div>🛒</div><div class="price">$250.00</div></div></article>

<a class="btn-outline abs" href="#" style="left:537px;top:1578px;width:126px;height:48px">VIEW MORE</a>

<section class="promo abs">
  <div class="abs" role="img" aria-label="Smiling tradeswoman in red hard hat giving a thumbs up" style="left:40px;top:-35px;width:400px;height:495px;background:linear-gradient(180deg,#d2322a 0%,#c9a58a 30%,#6f8aa8 60%,#7d93ac 100%);border-radius:160px 160px 0 0"></div>
  <div class="display abs" style="left:490px;top:133px;font-size:26px;line-height:1;color:var(--orange)">CUSTOMIZED</div>
  <div class="display abs" style="left:488px;top:174px;font-size:45px;line-height:1;color:#000">SAFETY UNIFORMS</div>
  <a class="btn-orange abs" href="#" style="left:494px;top:258px;width:193px;height:64px;font-size:18px">SHOP ONLINE</a>
</section>

<h2 class="sec-title display abs" style="top:2270px;font-size:36px">OUR TESTIMONILAS</h2>
<div class="rule abs" style="left:340px;top:2322px;width:336px"></div>
<div class="sec-sub abs" style="left:688px;top:2312px">REVIEWS</div>

<article class="review abs" style="left:145px"><div class="stars">★★★★★</div><p>Lorem ipsum dolor sit amet, conse ctetuer adipiscing elit. Aenean comodo ligula eget dolor. Aenean massa. Cum sociis</p><hr><div class="avatar" role="img" aria-label="Customer portrait"></div><div class="who">Marcus Reed</div></article>
<article class="review abs" style="left:473px"><div class="stars">★★★★★</div><p>Lorem ipsum dolor sit amet, conse ctetuer adipiscing elit. Aenean comodo ligula eget dolor. Aenean massa. Cum sociis</p><hr><div class="avatar" role="img" aria-label="Customer portrait"></div><div class="who">Dana Holt</div></article>
<article class="review abs" style="left:798px"><div class="stars">★★★★★</div><p>Lorem ipsum dolor sit amet, conse ctetuer adipiscing elit. Aenean comodo ligula eget dolor. Aenean massa. Cum sociis</p><hr><div class="avatar" role="img" aria-label="Customer portrait"></div><div class="who">Priya Lane</div></article>
<div class="quote abs" style="left:122px;top:2425px"><svg width="22" height="18" viewBox="0 0 22 18" fill="#fff"><path d="M0 18V9C0 3 4 0 9 0v4c-3 0-4 2-4 5h4v9zM12 18V9c0-6 4-9 9-9v4c-3 0-4 2-4 5h4v9z"/></svg></div>
<div class="quote abs" style="left:450px;top:2425px"><svg width="22" height="18" viewBox="0 0 22 18" fill="#fff"><path d="M0 18V9C0 3 4 0 9 0v4c-3 0-4 2-4 5h4v9zM12 18V9c0-6 4-9 9-9v4c-3 0-4 2-4 5h4v9z"/></svg></div>
<div class="quote abs" style="left:775px;top:2425px"><svg width="22" height="18" viewBox="0 0 22 18" fill="#fff"><path d="M0 18V9C0 3 4 0 9 0v4c-3 0-4 2-4 5h4v9zM12 18V9c0-6 4-9 9-9v4c-3 0-4 2-4 5h4v9z"/></svg></div>

<a class="btn-outline abs" href="#" style="left:537px;top:2713px;width:126px;height:48px">VIEW MORE</a>

<section class="gallery abs">
  <div class="tile abs" role="img" aria-label="High visibility clothing" style="left:118px;background:linear-gradient(135deg,#3a2a25,#c8582a 55%,#6e3b2a)"></div>
  <div class="tile abs" role="img" aria-label="Safety boots" style="left:363px;background:linear-gradient(135deg,#e6e6e6,#4c3f2c 55%,#e6e6e6)"></div>
  <div class="tile abs" role="img" aria-label="Protective gloves" style="left:606px;background:linear-gradient(135deg,#dfe3e8,#b6524a 55%,#d5dae0)"></div>
  <div class="tile abs" role="img" aria-label="Protective helmet" style="left:849px;background:linear-gradient(180deg,#2f7ec9,#d9c22c 60%,#f0f0f0)"></div>
  <div class="arrow abs" style="left:45px;background:var(--orange)"><svg width="18" height="14" viewBox="0 0 18 14" fill="none" stroke="#fff" stroke-width="2.4"><path d="M17 7H2M7 1L1 7l6 6"/></svg></div>
  <div class="arrow abs" style="left:1115px;background:#000"><svg width="18" height="14" viewBox="0 0 18 14" fill="none" stroke="#fff" stroke-width="2.4"><path d="M1 7h15M11 1l6 6-6 6"/></svg></div>
</section>

<h2 class="display abs" style="left:0;width:1200px;text-align:center;top:3353px;font-size:33px;line-height:1;color:#000">OUR NEWSLETTER SIGN UP</h2>
<p class="abs" style="left:0;width:1200px;text-align:center;top:3410px;font-size:13px">Subscribe our newsletter to get the latest collections and updates</p>

<footer class="footer abs"></footer>
<div class="newsbox abs"></div>
<div class="input abs">Enter Email Address</div>
<a class="btn-orange abs" href="#" style="left:709px;top:3461px;width:172px;height:65px;border-radius:33px;font-size:19px;font-weight:500">SIGNUP</a>

<div class="brand abs" style="left:128px;top:3688px">STEELGUARD<small>WORKWEAR</small></div>
<div class="social"><span style="left:155px"></span><span style="left:190px"></span><span style="left:225px"></span><span style="left:260px"></span></div>

<div class="col"><h5 style="left:451px;top:3645px">HELP &amp; SUPPORT</h5>
<ul style="left:451px;top:3690px"><li>Shipping &amp; Delivery</li><li>Terms &amp; Conditions</li><li>Privacy Policy</li><li>Returns</li></ul></div>
<div class="col"><h5 style="left:675px;top:3645px">QUICK LINKS</h5>
<ul style="left:675px;top:3690px"><li>Shop</li><li>Products</li><li>About Us</li><li>FAQ</li><li>Contact Us</li></ul></div>
<div class="col"><h5 style="left:857px;top:3645px">CONTACT DETAILS</h5></div>
<div class="contact" style="top:3695px"><div class="ci"><svg width="14" height="14" viewBox="0 0 14 14" fill="#fff"><path d="M3 0l3 3-2 2c1 2 3 4 5 5l2-2 3 3-2 3C6 14 0 8 0 3z"/></svg></div><div>CALL US<br>0400 123 987</div></div>
<div class="contact" style="top:3743px"><div class="ci"><svg width="14" height="10" viewBox="0 0 14 10" fill="#fff"><path d="M0 0h14L7 5zM0 2l7 5 7-5v8H0z"/></svg></div><div>EMAIL US<br>hello@steelguardwear.com</div></div>
<div class="contact" style="top:3791px"><div class="ci"><svg width="12" height="16" viewBox="0 0 12 16" fill="#fff"><path d="M6 0a6 6 0 0 1 6 6c0 4-6 10-6 10S0 10 0 6a6 6 0 0 1 6-6z"/><circle cx="6" cy="6" r="2" fill="var(--orange)"/></svg></div><div>Address line here dummy<br>Address line here</div></div>

<div class="bottom abs"><span class="abs" style="left:76px;top:18px">Copyright ©2024– All Rights Reserved by Company name</span>
<div class="pay"><span style="left:964px;background:#ddd"></span><span style="left:998px;background:#c9c9c9"></span><span style="left:1032px;background:#e8e8e8"></span><span style="left:1066px;background:#bfcfe6"></span><span style="left:1100px;background:#eee"></span></div></div>

</body>
</html>
```